Simple HVAC & Electrical Contractor Billboard

Leasing a 12'3" H by 49'3" W billboard. I'd like to use our current logo and add a few words to let people know what we do. Looking for a clean simple look.
Our company name is Harold Quince Mechanical - What we are is Air Conditioning & Electrical Contractors.

Our license numbers are TACLA00052618K & TECL71204 they will need to be visible on the sign somewhere.

I'm not sure how much information I want to see on the sign. I want to keep it clean but some of our contact info is as follows. Office # 682-540-9263 - Webpage hqmbrixel.com. I feel like most people can search the name to find the contact info they need but I'll defer to the designers to come up with the best design.

I have attached a couple different logos we have used I the past.

```html
<!DOCTYPE html>
<html lang="en">
<head>
<meta charset="utf-8">
<title>Harold Quince Mechanical – Billboard</title>
<link rel="stylesheet" href="https://fonts.googleapis.com/css2?family=Lato:wght@700;900&family=Kanit:wght@400;600&display=swap">
<style>
  :root {
    --page: #ffffff;
    --ink: #111111;
    --charcoal-dark: #141517;
    --charcoal-light: #3a3c3f;
    --strip-grey: #3d3d3d;
    --brand-red: #ec1c24;
    --paper: #ffffff;
  }
  html, body {
    margin: 0;
    padding: 0;
    width: 1200px;
    height: 1025px;
    overflow: hidden;
    background: var(--page);
  }
  .canvas {
    position: relative;
    width: 1200px;
    height: 1025px;
  }
  .billboard {
    position: absolute;
    left: 40px;
    top: 373px;
    width: 1120px;
    height: 279px;
    display: block;
    box-shadow: 0 2px 6px rgba(0,0,0,0.25);
  }
  .contact-phone, .contact-web, .service-line, .license-line {
    font-family: "Lato", sans-serif;
    font-weight: 900;
    fill: var(--paper);
  }
  .contact-web { font-weight: 700; }
  .service-line { font-weight: 700; }
  .service-line .minor { font-size: 36px; }
  .license-line { font-weight: 700; }
  .brand-name {
    font-family: "Kanit", sans-serif;
    font-weight: 600;
    fill: var(--ink);
  }
  .brand-tagline {
    font-family: "Kanit", sans-serif;
    font-weight: 400;
    fill: var(--brand-red);
  }
</style>
</head>
<body>
<main class="canvas">
  <svg class="billboard" viewBox="0 0 1874 467" xmlns="http://www.w3.org/2000/svg" aria-label="Harold Quince Mechanical billboard">
    <defs>
      <linearGradient id="charcoal" x1="0" y1="0" x2="1" y2="0">
        <stop offset="0" stop-color="var(--charcoal-light)"/>
        <stop offset="0.6" stop-color="var(--charcoal-dark)"/>
        <stop offset="1" stop-color="var(--charcoal-dark)"/>
      </linearGradient>
      <linearGradient id="top-strip" x1="0" y1="0" x2="1" y2="0">
        <stop offset="0" stop-color="var(--charcoal-dark)"/>
        <stop offset="0.4" stop-color="var(--charcoal-light)"/>
        <stop offset="1" stop-color="var(--charcoal-dark)"/>
      </linearGradient>
    </defs>

    <!-- base -->
    <rect class="panel-base" x="0" y="0" width="1874" height="467" fill="url(#charcoal)"/>
    <rect class="panel-top-strip" x="663" y="0" width="1211" height="37" fill="url(#top-strip)"/>

    <!-- white brand field -->
    <polygon class="brand-field" points="690,37 1874,37 1874,410 1080,410 942,194 785,194" fill="var(--paper)"/>

    <!-- red service band -->
    <polygon class="service-band" points="0,194 942,194 1080,410 0,410" fill="var(--brand-red)"/>

    <!-- bottom strips -->
    <rect class="license-strip" x="1080" y="410" width="794" height="57" fill="var(--strip-grey)"/>
    <polygon class="license-strip-edge" points="1080,410 1180,410 1180,467 1120,467" fill="var(--charcoal-dark)"/>
    <polygon class="accent-slash" points="926,410 1080,410 1120,467 958,467" fill="var(--paper)"/>

    <!-- contact -->
    <text class="contact-phone" x="68" y="102" font-size="76">682-540-9263</text>
    <text class="contact-web" x="68" y="157" font-size="46" textLength="550">WWW.HQMBRIXEL.COM</text>

    <!-- services -->
    <text class="service-line" x="70" y="264" font-size="44">AIR CONDITIONING &amp;</text>
    <text class="service-line" x="70" y="318" font-size="44">ELECTRICAL <tspan class="minor">CONTRACTORS &amp;</tspan></text>
    <text class="service-line" x="70" y="374" font-size="44">SPECIALIZING <tspan class="minor">IN SERVICE &amp; INSTALLATION</tspan></text>

    <!-- brand -->
    <rect class="brand-square" x="1385" y="65" width="200" height="200" fill="var(--brand-red)"/>
    <text class="brand-name" x="1182" y="352" font-size="72" textLength="608" lengthAdjust="spacingAndGlyphs">HAROLD QUINCE</text>
    <text class="brand-tagline" x="1790" y="382" font-size="29" text-anchor="end">Air Conditioning &amp; Electrical Contractors</text>

    <!-- license -->
    <text class="license-line" x="1788" y="450" font-size="30" text-anchor="end">LICENSE #: TACLA00052618K &amp; TECL71204</text>
  </svg>
</main>
</body>
</html>
```